Design an Awesome Metal Business Card!

Looking for an awesome design for a dual purpose business card that will be a giveaway to members.

A "grinder card" is a business like metal card that is used to grind herbs. We own a medical cannabis dispensary and will be giving away this business-grinder cards to our members.

This "metal business card" should incorporate our company branding and the wording: "Harbor Guild". Logo and or wording could be inked or etched. Be creative!!! SEE LOGO 'Harbor Guild" ATTACHED.

The most creative design will win this contest! Please see the following links for inspiration on branding. GOOD LUCK!

Link for format: https://brightslabpress.com/wp-content/uploads/2015/11/BSPR_Template_StainlessSteel.pdf

Links for design inspiration:
https://brightslabpress.com/portfolio/

```html
<!DOCTYPE html>
<html lang="en">
<head>
<meta charset="utf-8">
<title>Harbor Guild – Metal Grinder Card</title>
<link href="https://fonts.googleapis.com/css2?family=Roboto:wght@300;400;700;900&display=swap" rel="stylesheet">
<style>
  :root {
    --backdrop: #d9d6d2;
    --steel-light: #eef0f2;
    --steel-mid: #b9bcc0;
    --steel-dark: #7d8186;
    --etch: #3a3b3e;
    --band-top: #6e3b24;
    --band-bottom: #5a2e1b;
    --band-text: #d3c3b7;
    --band-text-soft: #bfa999;
  }
  * { margin: 0; padding: 0; box-sizing: border-box; }
  html, body { width: 1200px; height: 900px; overflow: hidden; }
  body {
    background: var(--backdrop);
    font-family: "Roboto", Arial, sans-serif;
  }
  .card {
    position: absolute;
    left: 110px; top: 170px;
    width: 980px; height: 560px;
    background: var(--steel-mid);
    overflow: hidden;
    box-shadow: 0 10px 30px rgba(0,0,0,.18);
  }
  .card__top-edge {
    position: absolute; left: 0; top: 0; width: 100%; height: 6px;
    background: var(--band-top);
  }
  .card__grinder-field {
    position: absolute; left: 0; top: 6px; width: 100%; height: 379px;
    background: linear-gradient(100deg, var(--steel-dark) 0%, var(--steel-mid) 35%, var(--steel-light) 70%, var(--steel-mid) 100%);
  }
  .brand {
    position: absolute; left: 190px; top: 130px;
    display: flex; align-items: center; gap: 30px;
  }
  .brand__name {
    font-weight: 900; font-size: 92px; letter-spacing: 1px;
    color: var(--etch);
  }
  .brand__dot {
    width: 110px; height: 110px; border-radius: 50%;
    background: var(--etch);
  }
  .card__band {
    position: absolute; left: 0; top: 385px; width: 100%; height: 175px;
    background: linear-gradient(180deg, var(--band-top), var(--band-bottom));
  }
  .contact-name {
    position: absolute; right: 574px; top: 60px; text-align: right;
  }
  .contact-name__name {
    font-weight: 700; font-size: 25px; color: var(--band-text); letter-spacing: .5px;
  }
  .contact-name__role {
    font-weight: 300; font-size: 21px; color: var(--band-text-soft); margin-top: 2px;
  }
  .contact-divider {
    position: absolute; left: 428px; top: 50px; width: 4px; height: 88px;
    background: var(--band-text);
  }
  .contact-lines {
    position: absolute; left: 458px; top: 52px;
    list-style: none;
    font-weight: 300; font-size: 22px; line-height: 29px; color: var(--band-text);
  }
</style>
</head>
<body>
  <div class="card">
    <div class="card__top-edge"></div>
    <div class="card__grinder-field" role="img" aria-label="Honeycomb grinder holes etched through brushed stainless steel"></div>
    <div class="brand">
      <span class="brand__name">Harbor Guild</span>
      <span class="brand__dot"></span>
    </div>
    <div class="card__band">
      <div class="contact-name">
        <div class="contact-name__name">JOHN DOE</div>
        <div class="contact-name__role">lawyer</div>
      </div>
      <div class="contact-divider"></div>
      <ul class="contact-lines">
        <li>M: +555.204.0187</li>
        <li>E:hello@harborguild.net</li>
        <li>W: www.harborguild.net</li>
      </ul>
    </div>
  </div>
</body>
</html>
```